2 Business Card Designs

Need two business cards designed:
1) for lumora studio (wedding video) website is lumorastudio.com.au
2) for lumora studio (corporate video) website is lumorastudio.net.au

I am looking for something simple, no fancy shapes etc. Just elegant, simple and classy.

Both companies are video companies, one specialising in weddings the other corporate videos. Neither card needs to have any pics of video or camera related images. Please use same colour schemes as respective websites.

Logo is the same but can change colour.

Industry/Entity Type

Camera

Requirements
Must have
• Logo should be either all white or a colour to match websites
Should not have
• swirls, flowers, shapes, etc.

```html
<!DOCTYPE html>
<html lang="en">
<head>
<meta charset="utf-8">
<title>Lumora Studio – Business Card</title>
<link rel="stylesheet" href="https://fonts.googleapis.com/css2?family=Questrial&display=swap">
<style>
  :root {
    --olive: #696a5c;
    --olive-dark: #5f6053;
    --cream: #e2e5c8;
    --card-light: #fbfcf6;
    --card-edge: #dadec2;
    --ink: #66675a;
    --page: #ffffff;
  }
  * { margin: 0; padding: 0; box-sizing: border-box; }
  html, body {
    width: 1200px; height: 800px; overflow: hidden;
    background: var(--page);
    font-family: "Questrial", "Helvetica Neue", Arial, sans-serif;
  }
  .canvas { position: relative; width: 1200px; height: 800px; }

  .card {
    position: absolute;
    width: 539px; height: 331px;
    border-radius: 24px;
    overflow: hidden;
    box-shadow: 0 2px 6px rgba(0,0,0,0.18);
  }

  /* Front */
  .card--front {
    left: 38px; top: 191px;
    background: radial-gradient(ellipse 75% 85% at 45% 40%, var(--card-light) 0%, #f1f3e4 50%, var(--card-edge) 100%);
  }
  .brand-name {
    position: absolute; right: 20px; top: 18px;
    font-size: 44px; line-height: 1;
    color: var(--ink);
    letter-spacing: 0.5px;
  }
  .person { position: absolute; left: 18px; top: 148px; color: var(--ink); }
  .person__name { font-size: 34px; line-height: 1; }
  .person__role { font-size: 20px; line-height: 1; margin-top: 6px; }

  .contact {
    position: absolute; left: 282px; top: 152px;
    list-style: none; color: var(--ink);
    font-size: 12.5px; line-height: 1;
  }
  .contact li { display: flex; align-items: center; gap: 5px; height: 17px; }
  .contact svg { width: 11px; height: 11px; flex: none; }

  .web-band {
    position: absolute; left: 0; right: 0; bottom: 0; height: 64px;
    background: linear-gradient(90deg, var(--olive-dark), var(--olive) 50%, var(--olive-dark));
    border-top: 4px solid #ffffff;
    box-shadow: 0 -1px 0 #c9ccb4;
  }
  .web-band__url {
    position: absolute; left: 17px; top: 11px;
    font-size: 34px; line-height: 1;
    color: var(--cream);
    letter-spacing: 0.3px;
  }

  /* Back */
  .card--back {
    left: 622px; top: 278px;
    background: var(--olive);
    display: flex; align-items: center; justify-content: center;
  }
  .back-name {
    font-size: 66px; line-height: 1;
    color: var(--cream);
    letter-spacing: 1px;
  }
</style>
</head>
<body>
<div class="canvas">

  <section class="card card--front" aria-label="Business card front">
    <div class="brand-name">lumora studio</div>

    <div class="person">
      <div class="person__name">Reid Callister</div>
      <div class="person__role">Owner/Director</div>
    </div>

    <ul class="contact">
      <li>
        <svg viewBox="0 0 11 11" aria-hidden="true"><rect width="11" height="11" rx="2" fill="#66675a"/><path d="M3.2 2.6l1.2 1.4-.6.8c.4.9 1.1 1.6 2 2l.8-.6 1.4 1.2-.7 1c-2.6-.3-4.6-2.3-4.9-4.9z" fill="#fff"/></svg>
        <span>+61 2 9000 4127</span>
      </li>
      <li>
        <svg viewBox="0 0 11 11" aria-hidden="true"><rect width="11" height="11" rx="2" fill="#66675a"/><circle cx="5.5" cy="5.5" r="2.8" fill="none" stroke="#fff" stroke-width="1"/><circle cx="5.5" cy="5.5" r="1" fill="#fff"/></svg>
        <span>hello@lumorastudio.com.au</span>
      </li>
      <li>
        <svg viewBox="0 0 11 11" aria-hidden="true"><rect width="11" height="11" rx="2" fill="#66675a"/><path d="M5.5 2c-1.4 0-2.4 1-2.4 2.3 0 1.7 2.4 4.5 2.4 4.5s2.4-2.8 2.4-4.5C7.9 3 6.9 2 5.5 2z" fill="#fff"/><circle cx="5.5" cy="4.3" r=".9" fill="#66675a"/></svg>
        <span>118 Harbour Street, Lindfield, NSW 2070</span>
      </li>
    </ul>

    <div class="web-band">
      <div class="web-band__url">www.lumorastudio.com.au</div>
    </div>
  </section>

  <section class="card card--back" aria-label="Business card back">
    <div class="back-name">lumora studio</div>
  </section>

</div>
</body>
</html>
```